VKTO Meridian LLC Website

Basic website for a start up business in the defense and federal space. If we could have intelligence analysis and technology as a focus that would be great. Looking to use our core colors but a lighter set of web pages would be preferable

Target Market(s)

Defense

Coding

Coded - Design and coding required

Number of Pages Required

3 page

```html
<!DOCTYPE html>
<html lang="en">
<head>
<meta charset="utf-8">
<title>VKTO Meridian LLC</title>
<link href="https://fonts.googleapis.com/css2?family=Poppins:wght@300;400;500;600;700&display=swap" rel="stylesheet">
<style>
:root{
  --red:#c8043c;
  --ink:#1e1a1f;
  --text:#555058;
  --panel:#f3f1f4;
  --field:#f1eff2;
  --white:#ffffff;
}
*{box-sizing:border-box;margin:0;padding:0}
html,body{width:1200px;height:3123px;overflow:hidden;background:var(--white);font-family:'Poppins',sans-serif;color:var(--ink)}
.page{position:relative;width:1200px;height:3123px}
.abs{position:absolute}
.brand{font-family:'Poppins',sans-serif;font-weight:700;letter-spacing:1px;display:flex;align-items:center;gap:10px;color:var(--ink)}
.brand .dot{width:14px;height:14px;border-radius:50%;background:var(--red)}
.btn{position:absolute;display:flex;align-items:center;justify-content:center;background:var(--red);color:var(--white);border-radius:30px;font-weight:600;font-size:15px;text-transform:uppercase;letter-spacing:-.2px}
/* header */
.site-header{left:0;top:0;width:1200px;height:88px;background:var(--white)}
.site-header .brand{position:absolute;left:60px;top:28px;font-size:28px}
.nav a{position:absolute;top:36px;font-size:13px;font-weight:500;color:var(--ink);text-decoration:none}
.nav a.active{color:var(--red)}
.header-call{left:952px;top:18px;width:187px;height:52px;font-size:16px;text-transform:none;gap:8px}
/* hero */
.hero{left:0;top:88px;width:1200px;height:602px;overflow:hidden}
.hero-photo{position:absolute;inset:0;background:linear-gradient(180deg,#dcdcd8 0%,#bdb6ad 45%,#6e655e 100%)}
.hero-title{left:60px;top:222px;font-size:61px;font-weight:600;line-height:72px;color:var(--white);letter-spacing:-.5px}
.hero-text{left:61px;top:374px;width:440px;font-size:14px;line-height:26px;color:var(--white)}
.hero-btn{left:60px;top:476px;width:152px;height:46px}
.callbar{left:190px;top:651px;width:820px;height:75px;border-radius:38px;overflow:hidden;display:flex}
.callbar .call{width:474px;background:var(--red);color:var(--white);display:flex;align-items:center;justify-content:center;gap:10px;font-size:30px;font-weight:300}
.callbar .call b{font-weight:600}
.callbar .mail{flex:1;background:var(--ink);color:var(--white);display:flex;align-items:center;justify-content:center;gap:12px;font-size:23px;font-weight:300;border-radius:38px 0 0 38px;margin-left:-20px}
/* welcome */
.welcome-brand{left:0;width:1200px;top:826px;justify-content:center;font-size:32px}
.section-title{left:0;width:1200px;text-align:center;font-size:47px;font-weight:300;letter-spacing:-1px;text-transform:uppercase}
.section-title strong,.card-title strong{color:var(--red);font-weight:600}
.lead{left:190px;width:820px;text-align:center;font-size:14px;line-height:26.5px;color:var(--text)}
/* services */
.service{position:absolute;width:540px;height:450px}
.service.panel{background:var(--panel);padding:103px 45px 0 46px}
.card-title{font-size:39px;font-weight:300;letter-spacing:-.5px;text-transform:uppercase;line-height:1}
.card-text{margin-top:23px;font-size:14px;line-height:26.3px;color:var(--text);width:440px}
.card-btn{position:relative;margin-top:24px;width:153px;height:45px}
.photo-defense{background:linear-gradient(135deg,#8ea9c9 0%,#3f5d82 55%,#1e3048 100%)}
.photo-federal{background:linear-gradient(160deg,#a6c3ea 0%,#c9d6e4 50%,#7f8a96 100%)}
/* contact */
.field{position:absolute;background:var(--field);border-radius:4px;font-size:12.5px;color:#6a656d;padding:14px 13px}
/* footer */
.footer-wave{left:0;top:2740px;width:1200px;height:338px}
.footer-bottom{left:0;top:3078px;width:1200px;height:45px;background:var(--ink);color:#a9a4ab;font-size:12px;display:flex;align-items:center;justify-content:center}
.footer-bottom b{color:var(--white);font-weight:600}
.foot-head{font-size:12px;font-weight:600;color:var(--white);text-transform:uppercase}
.foot-list{list-style:none;font-size:12.5px;color:var(--white)}
.foot-list li{height:30px}
.foot-info{font-size:12.5px;line-height:19px;color:var(--white)}
.social{width:34px;height:34px;border-radius:50%;background:var(--white)}
.social.dark{background:var(--ink)}
.news-input{left:893px;top:2952px;width:247px;height:32px;border-radius:16px;background:#d8244f;color:var(--white);font-size:12px;padding:8px 13px}
.news-btn{left:893px;top:2996px;width:247px;height:33px;border-radius:17px;background:var(--white);color:var(--ink);font-size:12px;font-weight:600;display:flex;align-items:center;justify-content:center}
</style>
</head>
<body>
<div class="page">

  <header class="site-header abs">
    <div class="brand"><span class="dot"></span>VKTO MERIDIAN</div>
    <nav class="nav">
      <a class="active" style="left:568px">HOME</a>
      <a style="left:655px">ABOUT</a>
      <a style="left:751px">SERVICES</a>
      <a style="left:863px">CONTACT</a>
    </nav>
    <div class="btn header-call">
      <svg width="18" height="18" viewBox="0 0 24 24" fill="#fff"><path d="M6.6 10.8a15 15 0 0 0 6.6 6.6l2.2-2.2c.3-.3.7-.4 1-.2 1.1.4 2.3.6 3.6.6.6 0 1 .4 1 1V20c0 .6-.4 1-1 1A17 17 0 0 1 3 4c0-.6.4-1 1-1h3.5c.6 0 1 .4 1 1 0 1.3.2 2.5.6 3.6.1.3 0 .7-.2 1z"/></svg>
      123 456 7890
    </div>
  </header>

  <section class="hero abs">
    <div class="hero-photo" role="img" aria-label="Hazy city skyline with tall towers at sunrise"></div>
    <svg class="abs" style="left:0;top:0" width="1200" height="602" viewBox="0 0 1200 602">
      <defs><linearGradient id="heroShade" x1="0" y1="0" x2="0" y2="1"><stop offset="0" stop-color="#4a4849" stop-opacity=".96"/><stop offset="1" stop-color="#2a2726" stop-opacity=".82"/></linearGradient></defs>
      <path d="M0 0 H741 C680 200 600 420 466 602 H0 Z" fill="url(#heroShade)"/>
    </svg>
    <h1 class="hero-title abs" style="top:134px">Defense and<br>Federal Space</h1>
    <p class="hero-text abs" style="top:286px">Lorem Ipsum is simply dummy text of the printing and typesetting industry. Lorem Ipsum has been the industry's standard dummy text ever since the 1500</p>
    <div class="btn hero-btn" style="top:388px">Contact Us</div>
  </section>

  <div class="callbar abs">
    <div class="call">CALL US
      <svg width="44" height="44" viewBox="0 0 44 44" fill="none" stroke="#fff" stroke-width="2"><circle cx="22" cy="22" r="20"/><path d="M14 12h5l2 6-3 2a14 14 0 0 0 6 6l2-3 6 2v5c-10 1-19-8-18-18z"/></svg>
      <b>123 456 7890</b></div>
    <div class="mail">
      <svg width="30" height="22" viewBox="0 0 30 22" fill="none" stroke="#fff" stroke-width="2"><rect x="1" y="1" width="28" height="20" rx="2"/><path d="M1 2l14 11L29 2"/></svg>
      info@vktomeridian.com</div>
  </div>

  <div class="brand welcome-brand abs"><span class="dot"></span>VKTO MERIDIAN</div>
  <h2 class="section-title abs" style="top:888px">Welcome to <strong>VKTO Meridian LLC</strong></h2>
  <p class="lead abs" style="top:962px">Lorem Ipsum is simply dummy text of the printing and typesetting industry. Lorem Ipsum has been the industry's standard dummy text ever since the 1500s, when an unknown printer took a galley of type and scrambled it to make a type specimen book. It has survived not only five centuries, but also the leap into electronic typesetting, remaining essentially unchanged.</p>
  <div class="btn" style="left:524px;top:1094px;width:152px;height:45px">Read More</div>

  <div class="service photo-defense" style="left:60px;top:1229px" role="img" aria-label="Military analysts in uniform reviewing data on a laptop beside a drone"></div>
  <div class="service panel" style="left:600px;top:1229px">
    <h3 class="card-title">Defense <strong>Service</strong></h3>
    <p class="card-text">Lorem Ipsum is simply dummy text of the printing and typesetting industry. Lorem Ipsum has been the industry's standard dummy text ever since the 1500s, when an unknown printer took a galley of type and scrambled it to make a type specimen book. It has survived not only five centuries, but also the leap into electronic typesetting, remaining essentially unchanged.</p>
    <div class="btn card-btn">Read More</div>
  </div>
  <div class="service panel" style="left:60px;top:1679px">
    <h3 class="card-title">Federal <strong>Space</strong></h3>
    <p class="card-text">Lorem Ipsum is simply dummy text of the printing and typesetting industry. Lorem Ipsum has been the industry's standard dummy text ever since the 1500s, when an unknown printer took a galley of type and scrambled it to make a type specimen book. It has survived not only five centuries, but also the leap into electronic typesetting, remaining essentially unchanged.</p>
    <div class="btn card-btn">Read More</div>
  </div>
  <div class="service photo-federal" style="left:600px;top:1679px" role="img" aria-label="Domed capitol building with columns under a blue sky"></div>

  <h2 class="section-title abs" style="top:2214px">Get in <strong>Touch With Us</strong></h2>
  <p class="lead abs" style="left:290px;width:620px;top:2286px">Lorem Ipsum is simply dummy text of the printing and typesetting industry. Lorem Ipsum has been the industry's standard dummy text ever since the 1500.</p>
  <div class="field" style="left:292px;top:2376px;width:300px;height:44px">Name</div>
  <div class="field" style="left:607px;top:2376px;width:300px;height:44px">Contact No.</div>
  <div class="field" style="left:292px;top:2435px;width:615px;height:44px">Email</div>
  <div class="field" style="left:292px;top:2495px;width:615px;height:104px">Contact No.</div>
  <div class="btn" style="left:509px;top:2614px;width:182px;height:45px">Send Message</div>

  <svg class="footer-wave abs" viewBox="0 0 1200 338" preserveAspectRatio="none">
    <path d="M0 110 C300 30 620 -10 860 8 C1000 20 1110 45 1200 70 V338 H0 Z" fill="var(--red)"/>
  </svg>
  <div class="brand abs" style="left:60px;top:2926px;font-size:28px;color:#fff"><span class="dot" style="background:#fff"></span>VKTO MERIDIAN</div>
  <div class="social abs" style="left:60px;top:3004px" aria-label="Social profile"></div>
  <div class="social dark abs" style="left:105px;top:3004px" aria-label="Social profile"></div>
  <div class="social abs" style="left:150px;top:3004px" aria-label="Social profile"></div>

  <div class="foot-head abs" style="left:339px;top:2850px">Useful Links</div>
  <ul class="foot-list abs" style="left:338px;top:2893px">
    <li>Home</li><li>About</li><li>Service</li><li>Contact</li>
  </ul>

  <div class="foot-head abs" style="left:616px;top:2850px">Contact Info</div>
  <svg class="abs" style="left:619px;top:2898px" width="12" height="16" viewBox="0 0 12 16" fill="#fff"><path d="M6 0a6 6 0 0 0-6 6c0 4.5 6 10 6 10s6-5.5 6-10a6 6 0 0 0-6-6zm0 8.5A2.5 2.5 0 1 1 6 3.5a2.5 2.5 0 0 1 0 5z"/></svg>
  <p class="foot-info abs" style="left:646px;top:2891px;width:220px">Lorem Ipsum is simply dummy text and printing typesetting.</p>
  <svg class="abs" style="left:616px;top:2953px" width="15" height="15" viewBox="0 0 24 24" fill="#fff"><path d="M6.6 10.8a15 15 0 0 0 6.6 6.6l2.2-2.2c.3-.3.7-.4 1-.2 1.1.4 2.3.6 3.6.6.6 0 1 .4 1 1V20c0 .6-.4 1-1 1A17 17 0 0 1 3 4c0-.6.4-1 1-1h3.5c.6 0 1 .4 1 1 0 1.3.2 2.5.6 3.6.1.3 0 .7-.2 1z"/></svg>
  <p class="foot-info abs" style="left:646px;top:2951px">123 456 7890</p>
  <svg class="abs" style="left:616px;top:2993px" width="15" height="11" viewBox="0 0 30 22" fill="#fff"><path d="M0 0h30v3L15 13 0 3z M0 6l15 10L30 6v16H0z"/></svg>
  <p class="foot-info abs" style="left:646px;top:2988px">info@vktomeridian.com</p>

  <div class="foot-head abs" style="left:893px;top:2850px">Newsletter</div>
  <p class="foot-info abs" style="left:893px;top:2891px;width:240px">Subscribe to stay with us and update our latest news, service etc...</p>
  <div class="news-input abs">Enter email here...</div>
  <div class="news-btn abs">SUBSCRIBE NOW</div>

  <div class="footer-bottom abs">©&nbsp;<b>VKTO MERIDIAN</b>&nbsp;- 2022. All Rights Reserved.</div>
</div>
</body>
</html>
```